Copper Lantern Gin

The gin is 100% proof and men and anbody 18 - 30 year old will be a target market - the bottle is very distinctive and lends itself to a square label.

The bottle is curved with a large front face that lends itself to a striking design. There should be enough space around the label to show the black gin in the bottle as this is a feature.

The current bottle with the existing label is attached below as is the new glass bottle. The new gin will be coloured black.

Font styles to use
Decorative
Script

```html
<!DOCTYPE html>
<html lang="en">
<head>
<meta charset="utf-8">
<title>Copper Lantern Gin – Label</title>
<link rel="stylesheet" href="https://fonts.googleapis.com/css2?family=Sancreek&family=Pinyon+Script&family=Staatliches&display=swap">
<style>
  :root {
    --canvas: #ffffff;
    --label-black: #262422;
    --label-white: #ffffff;
    --gold: #b0893c;
    --gold-light: #d6b868;
    --ink: #1d1b1a;
    --rule: #2a2826;
  }
  html, body {
    margin: 0;
    padding: 0;
    width: 1000px;
    height: 1200px;
    overflow: hidden;
    background: var(--canvas);
  }
  .canvas {
    position: relative;
    width: 1000px;
    height: 1200px;
  }
  .label {
    position: absolute;
    left: 207px;
    top: 67px;
    width: 586px;
    height: 584px;
    background: var(--label-black);
  }
  .label-panel {
    position: absolute;
    left: 10px;
    top: 338px;
    width: 566px;
    height: 236px;
    background: var(--label-white);
  }
  .hero-illustration {
    position: absolute;
    left: 103px;
    top: 78px;
    width: 385px;
    height: 180px;
    border-radius: 40% 50% 20% 30%;
    background: radial-gradient(ellipse at 55% 55%, rgba(214,184,104,0.55), rgba(176,137,60,0.25) 60%, rgba(38,36,34,0) 80%);
  }
  .brand-name {
    position: absolute;
    left: 0;
    top: 0;
    width: 586px;
    height: 584px;
  }
  .brand-name text {
    font-family: "Sancreek", serif;
    fill: var(--gold);
  }
  .descriptor {
    position: absolute;
    left: 0;
    top: 478px;
    width: 586px;
    display: flex;
    align-items: center;
    justify-content: center;
    gap: 14px;
  }
  .descriptor .rule {
    width: 40px;
    height: 2px;
    background: var(--rule);
  }
  .descriptor .style-name {
    font-family: "Pinyon Script", cursive;
    font-size: 19px;
    font-weight: 700;
    color: var(--ink);
    margin: 0 4px;
  }
  .spec {
    position: absolute;
    top: 526px;
    font-family: "Staatliches", sans-serif;
    font-size: 19px;
    letter-spacing: 1px;
    color: var(--ink);
  }
  .spec-volume { left: 98px; }
  .spec-abv { right: 92px; }
  .emblem-illustration {
    position: absolute;
    left: 253px;
    top: 518px;
    width: 78px;
    height: 34px;
    border-radius: 40%;
    background: linear-gradient(90deg, #e8e6e3, #9c9894 50%, #e8e6e3);
  }
</style>
</head>
<body>
<main class="canvas">
  <section class="label">
    <div class="label-panel"></div>
    <div class="hero-illustration" role="img" aria-label="Gold line illustration of a prowling hound with a flame-like tail"></div>
    <svg class="brand-name" viewBox="0 0 586 584" aria-label="Copper Lantern">
      <text x="98" y="330" font-size="88" textLength="386" lengthAdjust="spacingAndGlyphs">COPPER</text>
      <text x="93" y="448" font-size="96" textLength="398" lengthAdjust="spacingAndGlyphs">LANTERN</text>
    </svg>
    <div class="descriptor">
      <span class="rule"></span>
      <span class="style-name">Navy Strength British Gin</span>
      <span class="rule"></span>
    </div>
    <span class="spec spec-volume">50 CL</span>
    <div class="emblem-illustration" role="img" aria-label="Small line illustration of the hound emblem"></div>
    <span class="spec spec-abv">57% ABV</span>
  </section>
</main>
</body>
</html>
```